Service Plan Sales Flyer

The Watchpost Depot (www.kelvarnguard.com) is a commercial security integrator that installs security cameras, access control, intrusion, two-way radios and perimeter security. We require a one page flyer for our service plan for new and existing customers. The price of the service plan is $299/yr and includes the following;
1. Discounted service rate of $118/hr
2. Free remote support ($85/hr without a plan)
3. Free remote training
4. Priority support

Please review our brochure attached and create a one page sales flyer with the end goal of having the client sign up for our annual service plan . The plan will automatically renew every year. Email sales@kelvarnguard.com.

Target Market(s)

commercial industrial clients - no residential

Industry/Entity Type

review our website at www.kelvarnguard.com

Colors
0054AA
0677BA
7BADD7
CADEEF
E8F1F8
EE7325
F08F49
F5BC92
FAE3D3
FDF4ED

Requirements
Must have
• call to action
Should not have
• too many colors

```html
<!DOCTYPE html>
<html lang="en">
<head>
<meta charset="utf-8">
<title>Commercial Security Integrator – Service Plan Flyer</title>
<link rel="stylesheet" href="https://fonts.googleapis.com/css2?family=Oswald:wght@500;700&family=Roboto:wght@400;500;700;900&display=swap">
<style>
  :root{
    --navy:#1d2c55;
    --red:#ea3f3a;
    --ink:#1d2c55;
    --paper:#ffffff;
    --backdrop:#e9eaec;
  }
  *{box-sizing:border-box;margin:0;padding:0}
  html,body{width:1200px;height:2704px;overflow:hidden;background:var(--backdrop);font-family:"Roboto",Arial,sans-serif;color:var(--ink)}
  .flyer{position:absolute;left:40px;top:486px;width:1120px;height:1732px;background:var(--paper);overflow:hidden;box-shadow:0 10px 30px rgba(0,0,0,.12)}
  .header{position:absolute;left:0;top:0;width:1120px;height:640px;background:var(--navy)}
  .photo{position:absolute;left:600px;top:0;width:520px;height:640px;
    background:linear-gradient(135deg,#3a4a6b 0%,#8a93a6 45%,#d9dde4 70%,#5b6a86 100%);
    clip-path:polygon(24% 0,100% 0,100% 100%,0 100%,0 45%)}
  .accent{position:absolute;background:var(--red)}
  .accent.a1{left:0;top:0;width:1120px;height:640px;clip-path:polygon(690px 0,716px 0,591px 288px,565px 288px)}
  .accent.a2{left:1040px;top:520px;width:80px;height:120px;clip-path:polygon(100% 0,100% 100%,0 100%)}
  .brand{position:absolute;left:60px;top:50px;display:flex;align-items:center;gap:16px}
  .brand-mark{width:38px;height:38px;background:var(--red)}
  .brand-name{font-family:"Oswald",sans-serif;font-weight:700;font-size:34px;color:#fff;letter-spacing:1px;text-transform:uppercase}
  .title{position:absolute;left:60px;top:150px;font-family:"Oswald",sans-serif;font-weight:700;text-transform:uppercase;color:#fff;line-height:1}
  .title .line{display:block;font-size:82px}
  .title .hl{color:var(--red);font-size:106px;margin:8px 0}
  .intro{position:absolute;left:60px;top:490px;width:470px;font-size:21px;line-height:1.4;color:#fff}
  .services-tab{position:absolute;left:0;top:672px;width:420px;height:70px;background:var(--red);color:#fff;font-family:"Oswald",sans-serif;font-weight:700;font-size:46px;line-height:70px;padding-left:60px}
  .services-rule{position:absolute;left:420px;top:738px;width:660px;height:4px;background:var(--red)}
  .services{position:absolute;left:40px;top:780px;width:1040px;display:flex;justify-content:space-between}
  .service{width:240px;text-align:center}
  .service-icon{width:130px;height:130px;margin:0 auto;border-radius:50%;background:var(--navy);border:6px solid var(--red);display:flex;align-items:center;justify-content:center}
  .service-label{margin-top:22px;font-weight:900;font-size:25px;line-height:1.15;text-transform:uppercase;color:var(--navy)}
  .plan{position:absolute;left:60px;top:1040px;width:560px}
  .plan-lead{font-weight:700;font-size:38px;color:var(--red);line-height:1.1;white-space:nowrap}
  .plan-price{display:flex;align-items:center;gap:16px;margin-top:10px}
  .plan-price .amount{font-weight:900;font-size:88px;color:var(--navy);line-height:1;white-space:nowrap}
  .plan-price .tail{font-weight:700;font-size:32px;color:var(--navy);line-height:1.1;white-space:nowrap}
  .benefits{list-style:none;margin-top:30px}
  .benefits li{display:flex;align-items:center;gap:18px;font-size:23px;color:var(--navy);margin-bottom:16px;white-space:nowrap}
  .tick{width:28px;height:28px;flex:none}
  .contacts{position:absolute;left:60px;top:1460px;list-style:none}
  .contacts li{display:flex;align-items:center;gap:22px;font-size:32px;font-weight:500;color:var(--navy);margin-bottom:14px;height:50px}
  .contact-icon{width:50px;height:50px;border-radius:50%;background:var(--navy);display:flex;align-items:center;justify-content:center;flex:none}
  .steps{position:absolute;left:632px;top:1050px;width:460px;height:620px;background:var(--red);border-radius:14px;overflow:hidden}
  .steps-head{height:150px;background:var(--navy);padding:22px 30px;color:#fff;display:flex;align-items:center;gap:16px}
  .steps-head .label{font-family:"Oswald",sans-serif;font-weight:700;font-size:46px;line-height:1}
  .steps-head .sub{display:block;font-size:14px;font-weight:500;margin-top:8px;letter-spacing:.5px}
  .steps-head .big{font-family:"Oswald",sans-serif;font-weight:700;font-size:104px;color:var(--red);line-height:1}
  .steps-head .easy{font-family:"Oswald",sans-serif;font-weight:700;font-size:30px;line-height:1.05}
  .step-list{list-style:none;padding:14px 30px}
  .step-list li{display:flex;align-items:center;gap:26px;height:90px}
  .step-num{font-family:"Oswald",sans-serif;font-weight:700;font-size:70px;color:#fff;width:44px}
  .step-text{font-weight:900;font-size:26px;line-height:1.1;color:var(--navy);text-transform:uppercase}
  .corner-left{position:absolute;left:0;bottom:0;width:110px;height:110px;background:var(--navy);clip-path:polygon(0 0,100% 100%,0 100%)}
  .corner-right{position:absolute;right:0;bottom:0;width:130px;height:130px;background:var(--red);clip-path:polygon(100% 0,100% 100%,0 100%)}
  .base-rule{position:absolute;left:0;bottom:0;width:1120px;height:10px;background:var(--navy)}
</style>
</head>
<body>
<main class="flyer">
  <section class="header">
    <div class="photo" role="img" aria-label="Photo of a business person using a laptop with security camera equipment and a monitor"></div>
    <div class="accent a1"></div>
    <div class="accent a2"></div>
    <div class="brand"><span class="brand-mark"></span><span class="brand-name">The Watchpost Depot</span></div>
    <h1 class="title"><span class="line">Commercial</span><span class="line hl">Security</span><span class="line">Integrator</span></h1>
    <p class="intro">We install security cameras, access control, intrusion, two-way radios and perimeter security.</p>
  </section>

  <div class="services-tab">OUR SERVICES</div>
  <div class="services-rule"></div>
  <section class="services">
    <div class="service">
      <div class="service-icon"><svg width="64" height="64" viewBox="0 0 64 64" fill="none" stroke="#fff" stroke-width="3"><rect x="14" y="28" width="36" height="28" rx="3"/><path d="M22 28v-8a10 10 0 0 1 20 0v8"/><circle cx="32" cy="42" r="4"/></svg></div>
      <div class="service-label">Access Control<br>&amp; Intercom</div>
    </div>
    <div class="service">
      <div class="service-icon"><svg width="64" height="64" viewBox="0 0 64 64" fill="none" stroke="#fff" stroke-width="3"><rect x="12" y="10" width="40" height="44" rx="3"/><path d="M24 40v-8a8 8 0 0 1 16 0v8zM20 40h24"/><line x1="32" y1="18" x2="32" y2="22"/></svg></div>
      <div class="service-label">Intrusion<br>Alarm</div>
    </div>
    <div class="service">
      <div class="service-icon"><svg width="64" height="64" viewBox="0 0 64 64" fill="none" stroke="#fff" stroke-width="3"><path d="M32 8l20 8v14c0 13-9 22-20 26C21 52 12 43 12 30V16z"/><path d="M23 32l7 7 12-13"/></svg></div>
      <div class="service-label">Perimeter<br>Security</div>
    </div>
    <div class="service">
      <div class="service-icon"><svg width="64" height="64" viewBox="0 0 64 64" fill="none" stroke="#fff" stroke-width="3"><path d="M8 22l36-10 6 16-36 10z"/><path d="M20 36l4 12H12M50 22l6-2v10l-4 1"/></svg></div>
      <div class="service-label">Surveillance<br>Cameras</div>
    </div>
  </section>

  <section class="plan">
    <p class="plan-lead">The price of the service plan is</p>
    <div class="plan-price"><span class="amount">$299/YR</span><span class="tail">and includes<br>the following</span></div>
    <ul class="benefits">
      <li><svg class="tick" viewBox="0 0 30 30" fill="none" stroke="#ea3f3a" stroke-width="3"><rect x="2" y="2" width="26" height="26" rx="3"/><path d="M8 15l5 5 9-10"/></svg>Discounted service rate of $118/hr</li>
      <li><svg class="tick" viewBox="0 0 30 30" fill="none" stroke="#ea3f3a" stroke-width="3"><rect x="2" y="2" width="26" height="26" rx="3"/><path d="M8 15l5 5 9-10"/></svg>Free remote support ($85/hr without a plan)</li>
      <li><svg class="tick" viewBox="0 0 30 30" fill="none" stroke="#ea3f3a" stroke-width="3"><rect x="2" y="2" width="26" height="26" rx="3"/><path d="M8 15l5 5 9-10"/></svg>Free remote training</li>
      <li><svg class="tick" viewBox="0 0 30 30" fill="none" stroke="#ea3f3a" stroke-width="3"><rect x="2" y="2" width="26" height="26" rx="3"/><path d="M8 15l5 5 9-10"/></svg>Priority support</li>
    </ul>
  </section>

  <ul class="contacts">
    <li><span class="contact-icon"><svg width="26" height="26" viewBox="0 0 24 24" fill="#fff"><path d="M6.6 10.8a15 15 0 0 0 6.6 6.6l2.2-2.2a1 1 0 0 1 1-.25 11.4 11.4 0 0 0 3.6.57 1 1 0 0 1 1 1V20a1 1 0 0 1-1 1A17 17 0 0 1 3 4a1 1 0 0 1 1-1h3.5a1 1 0 0 1 1 1c0 1.25.2 2.45.57 3.57a1 1 0 0 1-.25 1z"/></svg></span>1-800-555-0147</li>
    <li><span class="contact-icon"><svg width="26" height="26" viewBox="0 0 24 24" fill="none" stroke="#fff" stroke-width="2"><rect x="3" y="5" width="18" height="14" rx="2"/><path d="M3 7l9 6 9-6"/></svg></span>sales@kelvarnguard.com</li>
    <li><span class="contact-icon"><svg width="26" height="26" viewBox="0 0 24 24" fill="none" stroke="#fff" stroke-width="2"><circle cx="12" cy="12" r="9"/><path d="M3 12h18M12 3c3 3 3 15 0 18M12 3c-3 3-3 15 0 18"/></svg></span>www.kelvarnguard.com</li>
  </ul>

  <section class="steps">
    <div class="steps-head">
      <div><span class="label">SIGN UP</span><span class="sub">FOR OUR ANNUAL SERVICE PLAN</span></div>
      <span class="big">5</span>
      <span class="easy">EASY<br>STEPS</span>
    </div>
    <ol class="step-list">
      <li><span class="step-num">1</span><span class="step-text">Needs<br>Consultation</span></li>
      <li><span class="step-num">2</span><span class="step-text">Custom<br>Quote</span></li>
      <li><span class="step-num">3</span><span class="step-text">Installation</span></li>
      <li><span class="step-num">4</span><span class="step-text">Ongoing<br>Support</span></li>
      <li><span class="step-num">5</span><span class="step-text">Improvements<br>&amp; Updates</span></li>
    </ol>
  </section>

  <div class="base-rule"></div>
  <div class="corner-left"></div>
  <div class="corner-right"></div>
</main>
</body>
</html>
```